Tallow & Mersey Needs New Stationery / Letterhead Design

We need new stationery to match our new logo (attached). Tallow & Mersey is a 34 year old nationwide law firm located in Houston Tx. They do personal injury law and pharmaceutical litigation.

WE DO NOT NEED BUSINESS CARDS.

Attached are several different file formats of the new logo.

Reason: We will make a decision in the next couple days. Finalizing edits now. Thank you!

Target Market(s)

consumers who have been injured due to the negligence of another or by a pharmaceutical drug or defective medical device. Also co-counsel and opposing counsel (law firms0.

Industry/Entity Type

Law Firm

Requirements
Must have
• logo
• Tallow & Mersey, LLP
• 7183 Corvid Lane, Suite 1000
• Brenford, TX 75591
• Tel: (555) 408-1936
• Fax: (555) 408-2275
• www.tallowandmersey.example
• Must have colors in the logo.
• Make the font go with the logo - not necessarily the same, but something that goes well with it.

```html
<!DOCTYPE html>
<html lang="en">
<head>
<meta charset="utf-8">
<title>Tallow &amp; Mersey Stationery</title>
<link rel="stylesheet" href="https://fonts.googleapis.com/css2?family=Cinzel:wght@600&family=Montserrat:wght@400;700&family=Source+Sans+3:wght@400&display=swap">
<style>
  :root {
    --navy: #0f2650;
    --charcoal: #4a4a4c;
    --paper: #f3f3f4;
    --ground: #e2e2e3;
    --ink: #2a2a2a;
    --muted: #5a5a5a;
  }
  * { margin: 0; padding: 0; box-sizing: border-box; }
  html, body { width: 1200px; height: 790px; overflow: hidden; }
  body { background: var(--ground); position: relative; font-family: "Source Sans 3", sans-serif; }

  .sheet { position: absolute; background: var(--paper); overflow: hidden; }
  .letterhead { width: 412px; height: 578px; }
  .letterhead--back { left: 647px; top: 64px; }
  .letterhead--front { left: 556px; top: 145px; }
  .envelope { width: 422px; height: 202px; left: 74px; }
  .envelope--front { top: 252px; }
  .envelope--back { top: 472px; }

  .corner-block { position: absolute; left: 0; background: var(--navy); }
  .letterhead .corner-block { top: 44px; width: 43px; height: 43px; }
  .envelope .corner-block { top: 17px; width: 24px; height: 38px; }

  .brand { position: absolute; color: var(--navy); }
  .brand__name { font-family: "Cinzel", serif; font-weight: 600; color: var(--navy); white-space: nowrap; line-height: 1; }
  .brand__tagline { font-family: "Montserrat", sans-serif; font-size: 4.4px; letter-spacing: 0.9px; color: var(--charcoal); margin-top: 3px; white-space: nowrap; }
  .letterhead .brand { left: 54px; top: 60px; }
  .letterhead .brand__name { font-size: 15px; }
  .envelope .brand { left: 34px; top: 30px; }
  .envelope .brand__name { font-size: 13px; }
  .envelope .brand__tagline { font-size: 3.9px; }

  .contact-panel { position: absolute; right: 0; background: var(--charcoal); color: #fff; font-family: "Montserrat", sans-serif; display: flex; align-items: center; }
  .letterhead .contact-panel { top: 38px; width: 172px; height: 43px; padding: 0 6px 0 19px; }
  .envelope .contact-panel { top: 17px; right: 0; width: 153px; height: 38px; padding: 0 6px 0 17px; }
  .contact-panel__address { font-size: 4.6px; line-height: 1.35; }
  .contact-panel__firm { font-weight: 700; font-size: 5px; margin-bottom: 4px; }
  .contact-panel__divider { width: 0.6px; align-self: stretch; margin: 12px 5px 10px; background: rgba(255,255,255,0.7); }
  .contact-panel__list { list-style: none; font-size: 4.3px; line-height: 1.45; margin-top: 6px; }
  .contact-panel__list li::before { content: "•"; margin-right: 3px; }

  .footer-band { position: absolute; left: 0; right: 0; bottom: 0; display: flex; }
  .footer-band__navy { background: var(--navy); flex: 0 0 70%; }
  .footer-band__grey { background: var(--charcoal); flex: 1; }
  .letterhead .footer-band { height: 8px; }
  .envelope .footer-band { height: 7px; }
  .envelope .footer-band__navy { flex-basis: 88%; }

  .flap { position: absolute; left: 0; top: 0; width: 422px; height: 64px; }
  .flap__name { position: absolute; left: 0; right: 0; top: 22px; text-align: center; font-family: "Cinzel", serif; font-weight: 600; font-size: 15px; color: #fff; }

  .letter { position: absolute; left: 45px; top: 146px; width: 336px; font-size: 8px; line-height: 10px; color: var(--ink); }
  .letter p { margin-bottom: 10px; }
  .letter .letter__body { margin-bottom: 29px; }
  .signature-area { position: absolute; left: 282px; top: 448px; width: 80px; height: 52px; background: linear-gradient(135deg, #ececed, #e6e6e8); border-radius: 4px; }
</style>
</head>
<body>

  <section class="sheet letterhead letterhead--back" aria-label="Letterhead, second sheet">
    <div class="corner-block"></div>
    <div class="brand">
      <div class="brand__name">Tallow &amp; Mersey</div>
      <div class="brand__tagline">ATTORNEYS AT LAW / <em>Founded in 1984</em></div>
    </div>
    <div class="contact-panel">
      <div class="contact-panel__address">
        <div class="contact-panel__firm">TALLOW &amp; MERSEY</div>
        7183 Corvid Lane, Suite 1000<br>Brenford, TX 75591
      </div>
      <div class="contact-panel__divider"></div>
      <ul class="contact-panel__list">
        <li>Tel: (555) 408-1936</li>
        <li>Fax: (555) 408-2275</li>
        <li>Web: www.tallowandmersey.example</li>
      </ul>
    </div>
    <div class="footer-band"><span class="footer-band__navy"></span><span class="footer-band__grey"></span></div>
  </section>

  <section class="sheet letterhead letterhead--front" aria-label="Letterhead">
    <div class="corner-block"></div>
    <div class="brand">
      <div class="brand__name">Tallow &amp; Mersey</div>
      <div class="brand__tagline">ATTORNEYS AT LAW / <em>Founded in 1984</em></div>
    </div>
    <div class="contact-panel">
      <div class="contact-panel__address">
        <div class="contact-panel__firm">TALLOW &amp; MERSEY</div>
        7183 Corvid Lane, Suite 1000<br>Brenford, TX 75591
      </div>
      <div class="contact-panel__divider"></div>
      <ul class="contact-panel__list">
        <li>Tel: (555) 408-1936</li>
        <li>Fax: (555) 408-2275</li>
        <li>Web: www.tallowandmersey.example</li>
      </ul>
    </div>

    <div class="letter">
      <p>1800, Hollin Ridge Street<br>Marlow, CA 90991.</p>
      <p>January 29th, 2011</p>
      <p>Mr. Pellham<br>President, Pellham Children's Center<br>344 Larkspur Lane<br>Eastvale, NY 10991</p>
      <p>Dear Mr. Pellham:</p>
      <p class="letter__body">In the first paragraph, one needs to give a brief introduction of oneself. One should also give reference to the purpose of the letter in brief.The second paragraph needs to give the details of the letter and its need. This paragraph is mostly longer than the others and plays the main role in the letter. Keep the sentences short and to the point. Avoid using complex words and sentences.</p>
      <p>The third and last paragraph is the conclusion of the letter and can be kept short.</p>
      <p>Sincerely,</p>
      <p>(this is where the signature of the writer will be placed)</p>
      <p>Dana Whitcombe<br>Read more at Quillpost: http://www.quillpost.example/articles/professional-letter-format.html</p>
    </div>
    <div class="signature-area" role="img" aria-label="Handwritten signature of the writer"></div>

    <div class="footer-band"><span class="footer-band__navy"></span><span class="footer-band__grey"></span></div>
  </section>

  <section class="sheet envelope envelope--front" aria-label="Envelope, front">
    <div class="corner-block"></div>
    <div class="brand">
      <div class="brand__name">Tallow &amp; Mersey</div>
      <div class="brand__tagline">ATTORNEYS AT LAW / <em>Founded in 1984</em></div>
    </div>
    <div class="contact-panel">
      <div class="contact-panel__address">
        <div class="contact-panel__firm">TALLOW &amp; MERSEY</div>
        7183 Corvid Lane, Suite 1000<br>Brenford, TX 75591
      </div>
      <div class="contact-panel__divider"></div>
      <ul class="contact-panel__list">
        <li>Tel: (555) 408-1936</li>
        <li>Fax: (555) 408-2275</li>
        <li>Web: www.tallowandmersey.example</li>
      </ul>
    </div>
    <div class="footer-band"><span class="footer-band__navy"></span><span class="footer-band__grey"></span></div>
  </section>

  <section class="sheet envelope envelope--back" aria-label="Envelope, back">
    <svg class="flap" viewBox="0 0 422 64" aria-hidden="true">
      <polygon points="0,0 422,0 410,64 12,64" fill="var(--navy)"/>
    </svg>
    <div class="flap__name">Tallow &amp; Mersey</div>
    <div class="footer-band"><span class="footer-band__navy"></span><span class="footer-band__grey"></span></div>
  </section>

</body>
</html>
```